The Harbor Under the Silence: A Winding Odyssey

This is a memoir about my breakdown/breakthrough followed by a spiritual awakening in 2012, I found my guru Rushan Pelgari Das, Mother Ayahuasca, and my spiritual mother, Ishti. By 2013, I was headed for a spiritual adventure through India, Southeast India, and Nepal which lasted 14 months. I lived in ashrams, meditated and prayed in temples,, traveled by train and bus, met many enlightened beings and interesting people. During Vipassana, I discovered my true essence- the light of my soul. It is a book of travel, romance, and spiritual growth. My idea is a road lined with temples, etc. I am walking down the road and see myself at the end of the road, facing out, with a bright star in my heart center. I see the colors in muted yellows and other earth-tone hues. Marigolds are used everywhere in the temples to adorn statues and doorways and this speaks to me. The title of the book is about finding out who I am beyond my stories and it is also about how our story will reveal to us who we really are.

Target Market(s)

Spiritual seekers, adventurers, travelers

Industry/Entity Type

Spiritual

Font styles to use
Serif
Sans Serif
Other font styles liked:
• I’m open. I like simplicity

Colors
FFC000
F8CF3A
FAE287
FDF2CF
FEFAEE

Requirements
Must have
• My name: Helga Sorrel Tun, Earth tones, pastels, me or a likeness of me, room for ISBN on back cover
Nice to have
• In the photo uploads I drew an idea of what I would like, there is also the idea in the book
Should not have
• I am not a fan of bright colors and that's all I can select here. I like neutral colors, like browns, slate, creams, and whites. This reflects the dusty roads I took throughout my journey.

```html
<!DOCTYPE html>
<html lang="en">
<head>
<meta charset="utf-8">
<title>The Harbor Under the Silence — Book Cover</title>
<link rel="stylesheet" href="https://fonts.googleapis.com/css2?family=Cormorant+Garamond:ital,wght@0,500;1,500&display=swap">
<style>
  :root {
    --backdrop: #262626;
    --sand: #c3b29f;
    --sand-light: #d3c5b3;
    --glow: #fff9f0;
    --ink-light: #f4f1ec;
  }
  * { margin: 0; padding: 0; box-sizing: border-box; }
  html, body {
    width: 1200px; height: 1200px; overflow: hidden;
    background: var(--backdrop);
  }
  .cover {
    position: absolute;
    left: 218px; top: 26px;
    width: 764px; height: 1147px;
    background: var(--sand);
    overflow: hidden;
    font-family: "Cormorant Garamond", Georgia, serif;
    color: var(--ink-light);
  }
  .cover__light {
    position: absolute;
    left: 0; top: 420px;
    width: 764px; height: 560px;
    background:
      radial-gradient(ellipse 34% 30% at 50% 48%, var(--glow) 0%, rgba(255,249,240,0.85) 35%, rgba(255,249,240,0) 100%),
      radial-gradient(ellipse 62% 50% at 50% 48%, rgba(232,220,204,0.9) 0%, rgba(211,197,179,0.5) 55%, rgba(195,178,159,0) 100%);
  }
  .title-line {
    position: absolute;
    left: 0; width: 100%;
    text-align: center;
    font-size: 128px;
    font-weight: 500;
    line-height: 1;
    white-space: nowrap;
  }
  .title-line--1 { top: 78px; }
  .title-line--2 { top: 219px; }
  .title-line--3 { top: 362px; }
  .subtitle {
    position: absolute;
    left: 0; width: 100%; top: 981px;
    text-align: center;
    font-size: 48px;
    font-style: italic;
    font-weight: 500;
    letter-spacing: 3px;
    line-height: 1;
  }
  .author {
    position: absolute;
    left: 0; width: 100%; top: 1060px;
    text-align: center;
    font-size: 26px;
    font-weight: 500;
    letter-spacing: 3px;
    text-transform: uppercase;
    line-height: 1;
  }
</style>
</head>
<body>
  <main class="cover">
    <div class="cover__light" role="img" aria-label="Illustration of a woman seen from behind with arms outstretched, surrounded by radiant rays of light"></div>
    <h1 class="title">
      <span class="title-line title-line--1">The Harbor</span>
      <span class="title-line title-line--2">Under The</span>
      <span class="title-line title-line--3">Silence</span>
    </h1>
    <p class="subtitle">A Winding Odyssey</p>
    <p class="author">Helga Sorrel Tun</p>
  </main>
</body>
</html>
```